Stillbrook Real Estate A5 Flyer

A5 Flyer for print distribution.

Front (include attached photo and branding):
Stillbrook are a new face in the Shelley & Rossmoyne real estate market. The Stillbrook team are both Shelley ‘locals’ and are genuinely and sincerely committed to this community. They put people first and pursue exceptional outcomes for their clients. This is the founding vision of Stillbrook.

Values:
Outstanding Customer Service
Timely Communication
Integrity Always
People First
Exceptional Negotiation

If you’re thinking of selling, interested in a free market appraisal, or simply want to find out more about the Stillbrook team, please reach out to Derek or Owen for a chat. We’d love to shout you a coffee at The Lantern Coffee + Kitchen.

Stillbrook Real Estate
E: hello@stillbrookrealestate.com.au
W: stillbrookrealestate.com.au

Back (half the page about Derek, other half the page about Owen). Please include headshots (Owen is the younger one):

Owen Pritchard (Property Consultant):

Owen has an in-depth understanding of all things property & finance related. With a degree in property & finance, diploma in finance & mortgage broking, certificate IV in real estate practice, project management roles in residential property development, plus years of small business experience as co-founder/co-owner of The Lantern Coffee + Kitchen, his experience in managing competing demands and complex scenarios runs far and wide.

Owen also has experience in corporate negotiations which is proving to be a very beneficial skill set. Owen is deeply committed to people and pursuing exceptional outcomes for his clients. He has built a reputation as a man of his word who is genuine and sincere and willing to go above and beyond for his clients.

owen@stillbrookrealestate.com.au
0412 308 246

Derek Lyons (Director / Licensee):

Derek has worked in various roles inclusive of being a Real Estate Agent, Bank Manager, Financial Counsellor, Mortgage Broker, and previously a Commercial Pilot. He spent eight years in remote Western Australia, where he worked for an international mining company creating strategies to help support the well-being of employees. Derek’s focus in life has always been to help people. To him, it is always about the relationship. Derek gets enormous satisfaction from seeing individuals, families, and businesses thrive financially. He has become a skilled negotiator with extensive experience working for a number of corporations and private firms.
 
What differentiates Derek is his compassion and commitment to people. He works hard to be an excellent communicator with the aim of achieving great results. He  has extensive sales experience with incredible ability to push the boundaries, think outside the box and meet or surpass expectations. This is why his clients keep coming back and continue to refer well into the future. 

derek@stillbrookrealestate.com.au
0438 261 907

Target Market(s)

House Sellers / House Buyers

Industry/Entity Type

Real Estate

Colors
0054AA
0677BA
7BADD7
CADEEF
E8F1F8

Requirements
Must have
• Branding / logo, river photo, head shots, company details etc
Nice to have
• Design as per attached branding guide

```html
<!DOCTYPE html>
<html lang="en">
<head>
<meta charset="utf-8">
<title>Stillbrook Real Estate – A5 Flyer</title>
<link rel="stylesheet" href="https://fonts.googleapis.com/css2?family=Fira+Sans:wght@400;600;700&family=Hind:wght@400;500&family=Cormorant+Garamond:wght@500&display=swap">
<style>
:root{
  --backdrop:#b7b7b7;
  --paper:#ffffff;
  --ink:#0f1e2d;
  --text:#1c2530;
  --water-deep:#2e4f6e;
  --water-mid:#5a7fa0;
  --sky:#c9d6e2;
  --suit:#2c3e5e;
  --portrait-bg:#eef1f4;
}
*{margin:0;padding:0;box-sizing:border-box}
html,body{width:1200px;height:904px;overflow:hidden;background:var(--backdrop)}
.canvas{position:relative;width:1200px;height:904px;background:var(--backdrop)}
.page{position:absolute;top:79px;width:526px;background:var(--paper);overflow:hidden;color:var(--text)}
.page--front{left:58px;height:745px}
.page--back{left:617px;height:736px}

/* front */
.brand{position:absolute;top:31px;left:0;width:100%;display:flex;justify-content:center;align-items:center;gap:12px;z-index:2}
.brand__dot{width:43px;height:43px;border-radius:50%;background:var(--ink)}
.brand__name{font-family:"Cormorant Garamond",serif;font-weight:500;font-size:25px;letter-spacing:7px;color:var(--ink)}
.hero-photo{position:absolute;top:84px;left:0;width:100%;height:244px;
  background:linear-gradient(180deg,#ffffff 0%,var(--sky) 18%,#8a9a8c 32%,#6d7d6c 46%,var(--water-mid) 58%,var(--water-deep) 100%)}
.headline-band{position:absolute;top:328px;left:0;width:100%;height:79px;background:var(--ink);
  display:flex;align-items:center;justify-content:center;text-align:center}
.headline{font-family:"Fira Sans",sans-serif;font-weight:700;font-size:23px;line-height:30px;color:#fff;letter-spacing:-0.1px}
.intro,.cta{position:absolute;left:0;width:100%;text-align:center;font-family:"Hind",sans-serif;font-weight:500;font-size:12.6px;line-height:16.3px;color:var(--ink)}
.intro{top:418px}
.cta{top:650px;line-height:15.8px}
.values-title{position:absolute;top:486px;left:0;width:100%;text-align:center;font-family:"Fira Sans",sans-serif;font-weight:700;font-size:15px;color:var(--ink)}
.values-tree{position:absolute;top:510px;left:0}
.value-label{position:absolute;top:594px;width:110px;margin-left:-55px;text-align:center;font-family:"Hind",sans-serif;font-weight:500;font-size:12.8px;line-height:16px;color:var(--ink)}
.footer{position:absolute;left:0;bottom:0;width:100%;height:37px;background:var(--ink);display:flex;align-items:center;justify-content:center;gap:9px;
  font-family:"Hind",sans-serif;font-size:11px;color:#fff}
.footer__name{font-family:"Fira Sans",sans-serif;font-weight:600;margin-right:6px}
.footer__item{display:flex;align-items:center;gap:5px}

/* back */
.profile__title{position:absolute;left:33px;font-family:"Fira Sans",sans-serif;font-weight:400;font-size:17px;color:var(--ink);white-space:nowrap;z-index:2}
.profile__title b{font-weight:700;letter-spacing:-0.2px}
.profile__bio{position:absolute;left:33px;font-family:"Hind",sans-serif;font-size:12.2px;line-height:15.8px;color:var(--text);white-space:nowrap;z-index:2}
.profile__bio p+p{margin-top:15.8px}
.headshot{position:absolute;right:0;z-index:1;background:linear-gradient(180deg,var(--portrait-bg) 0%,var(--portrait-bg) 40%,#8795ab 62%,var(--suit) 100%)}
.contact-band{position:absolute;right:0;width:273px;height:50px;z-index:3}
.contact-band svg.band{position:absolute;inset:0}
.contact-line{position:absolute;right:38px;font-family:"Fira Sans",sans-serif;font-weight:600;font-size:11.5px;color:#fff;white-space:nowrap}
</style>
</head>
<body>
<div class="canvas">

  <section class="page page--front">
    <div class="hero-photo" role="img" aria-label="Aerial photo of the river foreshore with riverside homes, moored boats and the city skyline in the distance"></div>
    <div class="brand"><span class="brand__dot"></span><span class="brand__name">STILLBROOK</span></div>
    <div class="headline-band">
      <h1 class="headline">Stillbrook are a new face in the<br>Shelley &amp; Rossmoyne real estate market.</h1>
    </div>
    <p class="intro">The Stillbrook team are both Shelley ‘locals’ and are genuinely and sincerely<br>committed to this community. They put people first and pursue exceptional<br>outcomes for their clients. This is the founding vision of Stillbrook.</p>

    <h2 class="values-title">VALUES:</h2>
    <svg class="values-tree" width="526" height="80" viewBox="0 0 526 80" fill="none" stroke="#0f1e2d">
      <path d="M79 27V2H463V27M189 2V27M280 2V27M372 2V27" stroke-width="2.2"/>
      <g stroke-width="2.4" fill="#fff">
        <circle cx="79" cy="52" r="25"/><circle cx="189" cy="52" r="25"/><circle cx="280" cy="52" r="25"/><circle cx="372" cy="52" r="25"/><circle cx="463" cy="52" r="25"/>
      </g>
      <g stroke-width="1.3" stroke-linecap="round" stroke-linejoin="round" transform="translate(0,-28)">
        <circle cx="77" cy="80" r="6"/><path d="M68 82a9 9 0 0 1 18 0M69 92c2-4 14-4 16 0"/><rect x="82" y="68" width="9" height="6" rx="1"/>
        <rect x="177" y="71" width="15" height="10" rx="4"/><rect x="186" y="78" width="15" height="10" rx="4"/><path d="M181 84l-2 4M196 91l2-3"/>
        <path d="M266 78l7-4 7 5 7-5 7 4M268 80l8 8 4-3 4 3 8-8"/>
        <circle cx="372" cy="70" r="3.5"/><path d="M367 78h10v7h-2v9h-6v-9h-2zM362 94h20"/>
        <rect x="454" y="68" width="14" height="17" rx="1"/><path d="M458 76l3 3 5-5M451 90l7-4 5 3 5-3 7 4"/>
      </g>
    </svg>
    <span class="value-label" style="left:79px">Outstanding<br>Customer Service</span>
    <span class="value-label" style="left:189px">Timely<br>Communication</span>
    <span class="value-label" style="left:280px">Integrity<br>Always</span>
    <span class="value-label" style="left:372px">People<br>First</span>
    <span class="value-label" style="left:463px">Exceptional<br>Negotiation</span>

    <p class="cta">If you’re thinking of selling, interested in a free market appraisal, or simply want<br>to find out more about the Stillbrook team, please reach out to Derek or Owen<br>for a chat. We’d love to shout you a coffee at The Lantern Coffee + Kitchen.</p>

    <footer class="footer">
      <span class="footer__name">Stillbrook Real Estate</span>
      <span class="footer__item">
        <svg width="13" height="13" viewBox="0 0 14 14" fill="none" stroke="#fff" stroke-width="1"><circle cx="7" cy="7" r="6.3"/><rect x="3.6" y="4.8" width="6.8" height="4.6"/><path d="M3.6 4.8L7 7.5l3.4-2.7"/></svg>
        hello@stillbrookrealestate.com.au</span>
      <span class="footer__item">
        <svg width="13" height="13" viewBox="0 0 14 14" fill="none" stroke="#fff" stroke-width="1"><circle cx="7" cy="7" r="6.3"/><ellipse cx="7" cy="7" rx="2.8" ry="6.3"/><path d="M0.7 7h12.6M2 3.8h10M2 10.2h10"/></svg>
        stillbrookrealestate.com.au</span>
    </footer>
  </section>

  <section class="page page--back">
    <article class="profile">
      <h2 class="profile__title" style="top:30px"><b>OWEN PRITCHARD</b> (Property Consultant):</h2>
      <div class="profile__bio" style="top:54px">
        <p>Owen has an in-depth understanding of all things property &amp;<br>finance related. With a degree in property &amp; finance, diploma<br>in finance and mortgage broking, certificate IV in real estate<br>practice, project management roles in residential property<br>development, plus years of small business experience as<br>co-founder/co-owner of The Lantern Coffee + Kitchen, his<br>experience in managing competing demands and complex<br>scenarios runs far and wide.</p>
        <p>Owen also has experience in corporate negotiations<br>which is proving to be a very beneficial skill set.<br>Owen is deeply committed to people &amp; pursuing<br>exceptional outcomes for his clients. He has built<br>a reputation as a man of his word who is<br>genuine and sincere and willing to go<br>above and beyond for his clients.</p>
      </div>
      <div class="headshot" style="top:27px;width:138px;height:243px" role="img" aria-label="Headshot of Owen Pritchard, the younger consultant, in a navy suit and light blue shirt"></div>
      <div class="contact-band" style="top:270px">
        <svg class="band" width="273" height="50" viewBox="0 0 273 50"><path d="M22 0H273V50H0Z" fill="#0f1e2d"/></svg>
        <span class="contact-line" style="top:9px">0412 308 246</span>
        <span class="contact-line" style="top:28px">owen@stillbrookrealestate.com.au</span>
        <svg style="position:absolute;right:16px;top:9px" width="15" height="15" viewBox="0 0 14 14"><circle cx="7" cy="7" r="7" fill="#d5d9de"/><path d="M4.6 3.6l1.4-.2.8 2-1 .8a5 5 0 0 0 2 2l.8-1 2 .8-.2 1.4c-3 .4-6.2-2.8-5.8-5.8z" fill="#0f1e2d"/></svg>
        <svg style="position:absolute;right:16px;top:28px" width="15" height="15" viewBox="0 0 14 14"><circle cx="7" cy="7" r="7" fill="#d5d9de"/><rect x="3.5" y="4.8" width="7" height="4.6" fill="none" stroke="#0f1e2d" stroke-width="1"/><path d="M3.5 4.8L7 7.5l3.5-2.7" fill="none" stroke="#0f1e2d" stroke-width="1"/></svg>
      </div>
    </article>

    <article class="profile">
      <h2 class="profile__title" style="top:359px"><b>DEREK LYONS</b> (Director / Licensee):</h2>
      <div class="profile__bio" style="top:383px">
        <p>Derek has worked in various roles inclusive of being a Real Estate Agent, Bank<br>Manager, Financial Counsellor, Mortgage Broker, &amp; previously<br>a Commercial Pilot. He spent eight years in remote Western<br>Australia, where he worked for an international mining<br>company creating strategies to help support the well-being<br>of employees. Derek’s focus in life has always been to help<br>people. To him, it is always about the relationship. Derek gets<br>enormous satisfaction from seeing individuals, families, and<br>businesses thrive financially. He has become a skilled<br>negotiator with extensive experience working for<br>a number of corporations and private firms.</p>
        <p>What differentiates Derek is his compassion and<br>commitment to people. He works hard to be<br>an excellent communicator with the aim of<br>achieving great results. He has extensive sales<br>experience with incredible ability to push the<br>boundaries, think outside the box and<br>meet or surpass expectations. This is<br>why his clients keep coming back &amp;<br>continue to refer well into the future.</p>
      </div>
      <div class="headshot" style="top:420px;width:138px;height:250px" role="img" aria-label="Headshot of Derek Lyons, the director, in a navy suit, white shirt and striped tie"></div>
      <div class="contact-band" style="top:670px">
        <svg class="band" width="273" height="50" viewBox="0 0 273 50"><path d="M22 0H273V50H0Z" fill="#0f1e2d"/></svg>
        <span class="contact-line" style="top:9px">0438 261 907</span>
        <span class="contact-line" style="top:28px">derek@stillbrookrealestate.com.au</span>
        <svg style="position:absolute;right:16px;top:9px" width="15" height="15" viewBox="0 0 14 14"><circle cx="7" cy="7" r="7" fill="#d5d9de"/><path d="M4.6 3.6l1.4-.2.8 2-1 .8a5 5 0 0 0 2 2l.8-1 2 .8-.2 1.4c-3 .4-6.2-2.8-5.8-5.8z" fill="#0f1e2d"/></svg>
        <svg style="position:absolute;right:16px;top:28px" width="15" height="15" viewBox="0 0 14 14"><circle cx="7" cy="7" r="7" fill="#d5d9de"/><rect x="3.5" y="4.8" width="7" height="4.6" fill="none" stroke="#0f1e2d" stroke-width="1"/><path d="M3.5 4.8L7 7.5l3.5-2.7" fill="none" stroke="#0f1e2d" stroke-width="1"/></svg>
      </div>
    </article>
  </section>

</div>
</body>
</html>
```